Step Boldly Toward Gain Promotional Flyer

I Need a one page, one-sided 8.5 x 11 editable promotional flyer that POPS!, designed in photoshop

[TITLE]Step Boldly Toward Gain: 3 BOLD Moves to Up-Level Your Business Now!

[CONTENT for the Flyer:]

At this content-rich event you will learn how to:
• Get out of feast and famine mode and into six, multi-six and/or seven figure-income mode
• Leapfrog your competition and become the obvious choice in your market
• Have your business aligned with who you are and what you want
• Enjoy your business far more than you imagined possible.
• Have more fun and time to yourself
• Live free and unbound!

Accolades
“Delphine helped us increase our six figure income by 41%...I feel reborn!” Marlene & Otis Pruitt, Vienna, VA

“…Delphine is a joy to listen to - compelling, smart, provocative…” – Dennis Ashcombe, Charlotte, North Carolina

“Delphine helped me increase my business by 66%...without me spending more time, money, or making cold calls! …I am in the zone!” Tina Worsley, Baltimore, MD
“Delphine is an energetic and dynamic speaker…content-rich…holds your attention to the very end!” Neil Barrow, Frmr Pres., Crane & Whitby, MD, MD, D.C., PA, DE, NJ
“Delphine is the real estate whisperer!” Hal Drummond, Washington D.C.

“Delphine was prepared, funny, informative and made a connection with each of our agents…Fabulous!…even my admins were PUMPED!!! – Paul Venable, New York

About Delphine:
Delphine is a highly regarded business development speaker & coach who knows how to pump up an audience and have them making more money, in less time, AND having more fun doing it! What’s not to love?! Consistently rated as an exceptional speaker and conference favorite! Among her work: Standout Method: How to Draw Your Best Buyers Time after Time!, Contact Sourcing Done Easy, The Worst Outreach Errors Real Estate Agents Commit and How to Steer Clear of Them, Slow Seasons Build Sharp Sellers, Drive Within the Head for Real Estate Agents.

[Also need a section for:]
Date: December 9, 2015, Time: 9:00 Am - 12:00 Noon, Place: Harbor Lantern Convention, Green Castle, PA

Target Market(s)

Real Estate Agents

Industry/Entity Type

Real Estate Agent

Font styles to use
Sans Serif

Colors
0655a3
f37122

Requirements
Must have
• the peak tier realty mentor logo
Nice to have
• step boldly toward gain logo; lots of POP! :-) ; open to other colors, accent colors.

```html
<!DOCTYPE html>
<html lang="en">
<head>
<meta charset="utf-8">
<title>Step Boldly Toward Gain – Event Flyer</title>
<link rel="stylesheet" href="https://fonts.googleapis.com/css2?family=Signika:wght@400;600;700&family=Open+Sans:ital,wght@0,400;0,600;1,400;1,600&display=swap">
<style>
  :root {
    --navy: #1c3560;
    --blue: #0655a3;
    --blue-deep: #16296a;
    --orange: #f37122;
    --white: #ffffff;
    --crowd: #e6e6e6;
  }
  html, body { margin: 0; padding: 0; overflow: hidden; }
  body { width: 907px; height: 1200px; background: var(--white); }
  .flyer {
    position: relative; width: 907px; height: 1200px; overflow: hidden;
    background: var(--white);
    font-family: "Open Sans", Arial, sans-serif;
  }
  .crowd-photo {
    position: absolute; left: 300px; top: 0; width: 607px; height: 680px;
    background: radial-gradient(ellipse at 55% 40%, #f6f6f6 0%, var(--crowd) 55%, #d2d2d2 100%);
  }
  .speaker-photo {
    position: absolute; left: 0; top: 0; width: 432px; height: 655px;
    background: linear-gradient(180deg, #c9a46a 0%, #d9b58c 30%, #efe9e3 58%, #2a2a2e 80%, #1e1e22 100%);
  }
  .shapes { position: absolute; left: 0; top: 0; }
  .brand {
    position: absolute; left: 345px; top: 140px;
    display: flex; align-items: center; gap: 8px;
    font-family: "Signika", Arial, sans-serif; font-weight: 600; font-size: 22px; color: var(--navy);
  }
  .brand-dot { width: 14px; height: 14px; border-radius: 50%; background: var(--orange); }
  .title {
    position: absolute; left: 372px; top: 200px; margin: 0;
    font-family: "Signika", Arial, sans-serif; font-weight: 600; font-size: 38px;
    line-height: 46px; color: var(--navy);
  }
  .bold-band {
    position: absolute; left: 345px; top: 300px; width: 562px; height: 78px;
    background: var(--orange);
  }
  .bold-band span {
    position: absolute; left: 27px; top: -10px;
    font-family: "Signika", Arial, sans-serif; font-weight: 700; font-size: 80px; color: var(--white);
    line-height: 96px;
  }
  .subtitle {
    position: absolute; left: 372px; top: 388px; margin: 0;
    font-family: "Signika", Arial, sans-serif; font-weight: 600; font-size: 27px;
    line-height: 34px; color: var(--navy);
  }
  .details {
    position: absolute; left: 444px; top: 482px; margin: 0;
    font-style: italic; font-size: 22px; line-height: 38px; color: #1a1a1a;
  }
  .details .indent { padding-left: 68px; }
  .learn-box {
    position: absolute; left: 58px; top: 672px; width: 384px;
    background: var(--orange); border-radius: 0 0 22px 22px;
    padding: 8px 12px 18px 22px; box-sizing: border-box; color: var(--white);
  }
  .learn-box h2 {
    margin: 0 0 12px; font-family: "Signika", Arial, sans-serif; font-weight: 600;
    font-size: 22px; line-height: 26px;
  }
  .learn-box ul { margin: 0; padding: 0 0 0 16px; list-style: none; }
  .learn-box li {
    position: relative; font-size: 12.2px; line-height: 16px; margin-bottom: 7px;
  }
  .learn-box li:last-child { margin-bottom: 0; }
  .learn-box li::before {
    content: ""; position: absolute; left: -14px; top: 5px; width: 6px; height: 6px;
    border-radius: 50%; background: var(--navy);
  }
  .about-tab {
    position: absolute; left: 674px; top: 706px; width: 233px; height: 36px;
    background: var(--orange); border-radius: 18px 0 0 18px;
    font-family: "Signika", Arial, sans-serif; font-weight: 600; font-size: 22px;
    line-height: 36px; color: var(--navy); padding-left: 16px; box-sizing: border-box;
  }
  .about-text {
    position: absolute; left: 470px; top: 750px; width: 410px; margin: 0;
    font-size: 11.8px; line-height: 15.4px; color: var(--white); text-align: justify;
  }
  .quote { position: absolute; margin: 0; }
  .quote p { margin: 0; font-style: italic; font-size: 14.5px; line-height: 21px; color: var(--white); }
  .quote cite {
    display: block; margin-top: 6px; font-style: italic; font-weight: 600; font-size: 12.5px; color: var(--orange);
  }
</style>
</head>
<body>
<div class="flyer">
  <div class="crowd-photo" role="img" aria-label="Faded photo of a cheering crowd of business people"></div>
  <div class="speaker-photo" role="img" aria-label="Portrait photo of Delphine, the speaker, in a dark blazer and white collar"></div>

  <svg class="shapes" width="907" height="1200" viewBox="0 0 907 1200" aria-hidden="true">
    <defs>
      <linearGradient id="lowerField" x1="0" y1="0" x2="1" y2="1">
        <stop offset="0" stop-color="#16296a"/>
        <stop offset="1" stop-color="#1d3f92"/>
      </linearGradient>
    </defs>
    <path d="M560 0 L907 0 L907 660 L760 660 C 910 520 920 220 560 0 Z" fill="var(--orange)"/>
    <path d="M470 0 C 870 70 935 330 878 520 C 850 610 795 650 720 668" fill="none" stroke="var(--blue-deep)" stroke-width="20"/>
    <path d="M0 640 Q 420 630 690 665 Q 830 675 907 590 L907 620 Q 830 700 690 680 Q 420 648 0 660 Z" fill="var(--white)"/>
    <path d="M0 660 Q 420 648 690 680 Q 830 700 907 620 L907 1200 L0 1200 Z" fill="url(#lowerField)"/>
  </svg>

  <div class="brand"><span class="brand-dot"></span>Step Boldly Toward Gain</div>

  <h1 class="title">Step Boldly<br>Toward Gain:</h1>
  <div class="bold-band"><span>3 BOLD</span></div>
  <p class="subtitle">Moves to Up-Level Your<br>Business Now!</p>

  <p class="details">
    Date: December 9, 2015,<br>
    Time: 9:00 Am - 12:00 Noon,<br>
    Place: Harbor Lantern Convention,<br>
    <span class="indent">Green Castle, PA</span>
  </p>

  <section class="learn-box">
    <h2>At this content-rich event you<br>will learn how to:</h2>
    <ul>
      <li>Get out of feast and famine mode and into six, multi-six and/or seven figure-income mode</li>
      <li>Leapfrog your competition and become the obvious choice in your market</li>
      <li>Have your business aligned with who you are and what you want</li>
      <li>Enjoy your business far more than you imagined possible.</li>
      <li>Have more fun and time to yourself</li>
      <li>Live free and unbound!</li>
    </ul>
  </section>

  <div class="about-tab">About Delphine:</div>
  <p class="about-text">Delphine is a highly regarded business development speaker &amp; coach who knows how to pump up an audience and have them making more money, in less time, AND having more fun doing it! What’s not to love?! Consistently rated as an exceptional speaker and conference favorite! Among her work: Standout Method: How to Draw Your Best Buyers Time after Time!, Contact Sourcing Done Easy, The Worst Outreach Errors Real Estate Agents Commit and How to Steer Clear of Them, Slow Seasons Build Sharp Sellers, Drive Within the Head for Real Estate Agents.</p>

  <blockquote class="quote" style="left:470px; top:905px; width:410px;">
    <p>“Delphine helped me increase my business by 66%...without me spending more time, money, or making cold calls! …I am in the zone!”</p>
    <cite>Tina Worsley, Baltimore, MD</cite>
  </blockquote>
  <blockquote class="quote" style="left:470px; top:1005px; width:410px;">
    <p>“Delphine is an energetic and dynamic speaker… content-rich…holds your attention to the very end!”</p>
    <cite>Neil Barrow, Frmr Pres., Crane &amp; Whitby, MD, MD, D.C., PA, DE, NJ</cite>
  </blockquote>
  <blockquote class="quote" style="left:470px; top:1085px; width:410px;">
    <p>“Delphine is the real estate whisperer!”</p>
    <cite>Hal Drummond, Washington D.C.</cite>
  </blockquote>

  <blockquote class="quote" style="left:58px; top:985px; width:384px;">
    <p>“Delphine helped us increase our six figure income by 41%...I feel reborn!”</p>
    <cite>Marlene &amp; Otis Pruitt, Vienna, VA</cite>
  </blockquote>
  <blockquote class="quote" style="left:58px; top:1070px; width:384px;">
    <p>“…Delphine is a joy to listen to - compelling, smart, provocative…”</p>
    <cite>Dennis Ashcombe, Charlotte, North Carolina</cite>
  </blockquote>
</div>
</body>
</html>
```